Elegant One-Page Flyer That Catches People's Eye

For a series of workshops and zoom calls I am marketing with a colleague of mine, we would like to have an elegant, catchy one-page flyer that entices people to contact us. I am envisioning a one-page flyer (a card that is somewhat larger than a postcard) with great text, layout and images which magnetically draws people to us and is positive and inspiring. Also, if at all possible, a QR code linking it to our websites. Good colours would be shades of blue and green. I am uploading: the Text, our pictures, logos and contact information.

```html
<!DOCTYPE html>
<html lang="en">
<head>
<meta charset="utf-8">
<title>Rising above Hidden Career Deal breakers</title>
<link rel="stylesheet" href="https://fonts.googleapis.com/css2?family=Carlito:wght@400;700&family=Archivo+Black&family=Open+Sans:wght@400&display=swap">
<style>
  :root {
    --pale-green: #dce37f;
    --lime: #aec922;
    --slate: #58584f;
    --ink: #3f4036;
    --quote-ink: #55564b;
    --soft-text: #cdd39a;
    --list-text: #e6e9c8;
    --white: #ffffff;
  }
  * { margin: 0; padding: 0; box-sizing: border-box; }
  html, body { width: 783px; height: 1200px; overflow: hidden; background: #fff; }
  .flyer {
    position: relative; width: 783px; height: 1200px; overflow: hidden;
    background: var(--pale-green); border: 1px solid var(--slate);
    font-family: "Carlito", "Calibri", sans-serif;
  }
  .backdrop { position: absolute; inset: 0; }
  .abs { position: absolute; white-space: nowrap; }

  .studio-name { left: 47px; top: 62px; font-size: 15px; color: var(--quote-ink); }
  .partner-name { left: 530px; top: 48px; font-size: 38px; color: var(--quote-ink); }

  .portrait-main { left: 16px; top: 105px; width: 180px; height: 203px; border-radius: 50%; border: 2px solid #111;
    background: radial-gradient(circle at 50% 40%, #d9b8a4 0%, #a07a68 40%, #eeeeee 75%); }

  .quote { left: 204px; top: 136px; font-size: 25.5px; font-weight: 700; color: var(--quote-ink); line-height: 32.5px; }
  .quote .mark { font-size: 18px; vertical-align: top; }
  .quote .lead { display: inline-block; width: 14px; }

  .title { left: 110px; width: 640px; top: 292px; text-align: center;
    font-family: "Archivo Black", "Arial Black", sans-serif; font-size: 33px; line-height: 47px; color: #262626; letter-spacing: .3px; }

  .format { left: 0; width: 783px; top: 400px; text-align: center; color: var(--white);
    font-family: "Open Sans", sans-serif; font-size: 29px; line-height: 41px; }

  .label-bar { left: 0; top: 533px; width: 604px; height: 31px; background: var(--lime); }
  .label-bar span { position: absolute; left: 39px; top: 3px; font-size: 21px; font-weight: 700; color: var(--ink); }

  .facilitators { left: 12px; top: 563px; width: 605px; list-style: none; }
  .facilitators li { position: relative; padding-left: 28px; font-size: 21px; line-height: 26.6px; color: var(--soft-text); white-space: nowrap; }
  .facilitators strong { color: var(--lime); font-weight: 700; }
  .arrow { position: absolute; left: 0; top: 8px; width: 20px; height: 11px; }

  .portrait-second { left: 623px; top: 537px; width: 157px; height: 235px;
    background: linear-gradient(160deg, #8a4a3a 0%, #5e4a3f 45%, #9a7aa6 80%, #6a5a68 100%); }
  .scene-climb { left: 1px; top: 811px; width: 267px; height: 184px;
    background: linear-gradient(180deg, #2d6eb8 0%, #a9c7e6 45%, #dfe9f3 60%, #5d6f82 85%, #2e3a46 100%); }

  .learn-box { left: 282px; top: 811px; width: 499px; height: 53px; background: var(--lime); }
  .learn-box p { position: absolute; left: 7px; top: 3px; font-size: 21.5px; line-height: 26.5px; font-weight: 700; color: var(--ink); white-space: nowrap; }

  .dealbreakers { left: 289px; top: 891px; list-style: none; font-size: 21.5px; line-height: 26.6px; color: var(--list-text); }
  .dealbreakers li::before { content: "• "; }

  .contact-bar { left: 0; top: 1022px; width: 733px; height: 35px; background: var(--lime); }
  .contact-bar span { position: absolute; left: 41px; top: 4px; font-size: 23.5px; font-weight: 700; color: var(--ink); white-space: nowrap; }

  .contacts { left: 43px; top: 1064px; list-style: none; }
  .contacts li { position: relative; padding-left: 32px; font-size: 28px; line-height: 32.5px; color: var(--lime); }
  .contacts .arrow { top: 11px; }
</style>
</head>
<body>
<div class="flyer">
  <svg class="backdrop" width="783" height="1200" viewBox="0 0 783 1200" aria-hidden="true">
    <path d="M200 289 Q392 218 565 289 Z" fill="var(--slate)"/>
    <path d="M0 393 H783 V1164 H0 Z" fill="var(--slate)"/>
    <path d="M0 393 H45 Q15 420 0 438 Z" fill="var(--pale-green)"/>
    <path d="M783 393 H722 Q760 420 783 458 Z" fill="var(--pale-green)"/>
    <rect x="0" y="289" width="783" height="104" fill="var(--lime)"/>
    <rect x="0" y="1164" width="783" height="36" fill="var(--lime)"/>
  </svg>

  <div class="abs studio-name">Northline Mentoring</div>
  <div class="abs partner-name">PathWell</div>

  <div class="abs portrait-main" role="img" aria-label="Portrait photo of Dr. Selma Brandt"></div>

  <p class="abs quote"><span class="lead"><span class="mark">“</span></span>Is your career going the way you want?<br><span class="lead"></span>If not, do you feel stuck? Blocked? Frustrated?<br><span class="lead"></span>Don’t know what to do about this?<span class="mark">”</span></p>

  <h1 class="abs title">Rising above Hidden Career<br>Deal breakers</h1>

  <p class="abs format">Format:<br>4 Mini-Workshops + 2 short Online Group<br>Coaching Sessions between Workshops</p>

  <div class="abs label-bar"><span>Facilitators:</span></div>
  <ul class="abs facilitators">
    <li><svg class="arrow" viewBox="0 0 20 11"><path d="M0 0H12L20 5.5 12 11H0L5 5.5Z" fill="var(--lime)"/></svg><strong>Dr. Maren Holloway,</strong><br>PhD, is an American &amp; Swiss-Trained Work &amp; Organizational<br>Psychologist, Accredited Career Coach, Board Certified<br>Hypnotherapist, Certified Naturopath &amp; Certified<br>Ayurvedic Practitioner.</li>
    <li><svg class="arrow" viewBox="0 0 20 11"><path d="M0 0H12L20 5.5 12 11H0L5 5.5Z" fill="var(--lime)"/></svg><strong>Dr. Selma Brandt</strong><br>Ph.D., is a coach and somatic experience practitioner , a<br>team coach with diploma and a certified virtual team coach.</li>
  </ul>

  <div class="abs portrait-second" role="img" aria-label="Photo of Dr. Maren Holloway standing before an autumn tree"></div>
  <div class="abs scene-climb" role="img" aria-label="Photo of a climber on a rope high above mountains and a bright sky"></div>

  <div class="abs learn-box"><p>Learn to overcome and rise above the 4 top hidden<br>career deal breakers fast:</p></div>
  <ul class="abs dealbreakers">
    <li>Microaggressions</li>
    <li>Toxic black box team dynamics</li>
    <li>Workplace snakes and other dysfunctional types</li>
    <li>Disempowering Subconscious Algorithms</li>
  </ul>

  <div class="abs contact-bar"><span>For&nbsp; dates, venue and further information contact Selma or Maren at:</span></div>
  <ul class="abs contacts">
    <li><svg class="arrow" viewBox="0 0 20 11"><path d="M0 0H12L20 5.5 12 11H0L5 5.5Z" fill="var(--lime)"/></svg>Selma – selma@northline.ch, 079 000 12 34.</li>
    <li><svg class="arrow" viewBox="0 0 20 11"><path d="M0 0H12L20 5.5 12 11H0L5 5.5Z" fill="var(--lime)"/></svg>Maren – maren@pathwell.ch, 076 000 5678</li>
  </ul>
</div>
</body>
</html>
```